Banner ad design for Vantora Display Ads

We are looking for a designer to develop a concept for banner ads for a Vantora Display campaign we are building.

We have 3 business lines, shredding services, records management services and scanning services.

We are looking for 4 sets of ads to be created, one for each business line + one set that showcases all of our lines together.

For the design concepts, we would like to see a few sizes (banner, square, leaderboard, skyscraper, etc) for each.

The person chosen will then need to create the ads into all Vantora supported sizes -- 20 sizes total for each set of ads as per the Vantora size guidelines found on this page - https://help.vantora-example.com/vantora-ads/answer/4827150?hl=en&ref_topic=6604821#

A few items to note:
- Design should complement our existing brand/website look and feel (www.oak-ferry.ca)
- Each final ad must be 150Kb or less in size
- Final designs should be editable, meaning if we would like to change some copy in the design, we can do so using a well-known software (Canva, Photoshop/InDesign, etc)
- Some images are attached for use, but if you feel a different stock image is more suitable to to your design, please go ahead and use it.

Provided below is some messaging that can be used for each set of ads. Do not feel you need to use all of the messaging, it is provided for guidance.

SHREDDING SERVICES:

Possible Short Headline:
-- One-Time Shredding Services
-- Secure Shredding Services
-- Affordable On-Site Shredding

Possible Long Headline
-- Your Paper Can be Destroyed as Soon as the Next Business Day

Possible Descriptions:
-- KVEC Gold Certified On site shredding company. Service as soon as Next Day.
-- Secure and Affordable Toronto & GTA On-Site Shredding.
-- Certified, Affordable Office Shredding Since 2003.
-- Quick, no contact and affordable paper shredding services in Toronto & Southern Ontario.
-- Certified, Affordable Office Shredding Since 2003. Fast, no contact shredding service.

Call to Action
-- Get a Quote

RECORDS MANAGEMENT
Short Headline:
-- Off-site Records Storage
-- Records Management & Storage
-- Secure Records Storage
-- Records Management Services
-- Long Term Records Management
-- Document Storage Solutions

Possible Description
-- Local, Affordable Storage Solutions. Protect and Store your Documents in our Secure Facility
-- Local, Affordable Records Management Solutions. Store your Records in our Secure Facility
-- Certified, Affordable Document Storage Since 2004. Contact Us for a Free Quote!
-- Vaultline+ Certified, Affordable Document Storage Since 2004. Contact Us for a Free Quote!

Call to Action
-- Get a Quote

SCANNING SERVICES

Short Headline:
-- Professional Scanning Company
-- Toronto & GTA Scanning Service
-- Document Scanning Services
-- Digital Conversion Services
-- Fast & Easy Retrieval

Description
-- Scan and documents and files with Professional scanning services from Oak-Ferry
-- Convert Your Paper Files to Electronic Files. Fast & Easy Retrieval.
-- Easily access your documents electronically with Document Scanning Services

Call to Action
-- Get a Quote

ALL SERVICES AD SET
Short Headline
-- Shred, Scan & Store Documents
-- Secure Shredding, Records Management and Scanning Services
-- #1 Document Management Company
-- Oak Ferry Shredding, Storage & Scanning

Description
-- Secure and Affordable Toronto & GTA On-Site Shredding, Document Storage & Scanning Company

Call to Action
-- Get a Quote

Font styles to use
Sans Serif

```html
<!DOCTYPE html>
<html lang="en">
<head>
<meta charset="utf-8">
<title>Oak-Ferry One-Time Shredding Banner Set</title>
<link href="https://fonts.googleapis.com/css2?family=Montserrat:wght@500;600;700;800;900&display=swap" rel="stylesheet">
<style>
  :root {
    --stage: #22558a;
    --brand-blue: #0b9bd7;
    --ink: #1f1f1f;
    --paper: #ffffff;
    --frame: #1b1b1b;
    --photo-top: #d9d4c8;
    --photo-mid: #bdb8ae;
    --photo-low: #8fb7c9;
  }
  * { box-sizing: border-box; margin: 0; padding: 0; }
  html, body { width: 1200px; height: 960px; overflow: hidden; }
  body {
    background: var(--stage);
    font-family: "Montserrat", Arial, sans-serif;
    color: var(--ink);
    position: relative;
  }
  .ad {
    position: absolute;
    background: var(--paper);
    border: 1px solid var(--frame);
    overflow: hidden;
  }
  .ad-skyscraper { left: 60px; top: 120px; width: 190px; height: 719px; }
  .ad-leaderboard { left: 289px; top: 120px; width: 873px; height: 107px; }
  .ad-square { left: 289px; top: 504px; width: 402px; height: 335px; }

  .headline { text-align: center; color: var(--brand-blue); font-weight: 800; text-transform: uppercase; line-height: 0.95; }
  .headline .lead { display: block; font-weight: 900; letter-spacing: -0.5px; }
  .headline .sub { display: block; }
  .tagline { text-align: center; font-weight: 600; color: var(--ink); }

  .photo {
    position: absolute;
    background: linear-gradient(180deg, var(--photo-top) 0%, var(--photo-mid) 55%, var(--photo-low) 100%);
  }
  .rule { position: absolute; background: var(--brand-blue); }

  .brand { position: absolute; text-align: left; }
  .brand-name {
    display: flex; align-items: center; gap: 4px;
    font-weight: 700; color: var(--ink); letter-spacing: -0.3px; line-height: 1;
  }
  .brand-mark { display: inline-block; background: var(--brand-blue); }
  .brand-line { display: block; font-weight: 500; color: var(--ink); margin-top: 3px; }

  .cta {
    position: absolute;
    display: flex; align-items: center; justify-content: center; gap: 10px;
    background: var(--brand-blue); color: var(--paper);
    font-weight: 700; text-transform: uppercase; border-radius: 20px;
    text-decoration: none;
  }
  .cta svg { display: block; }

  /* Skyscraper */
  .ad-skyscraper .brand { left: 22px; top: 26px; }
  .ad-skyscraper .brand-name { font-size: 24px; }
  .ad-skyscraper .brand-mark { width: 9px; height: 9px; }
  .ad-skyscraper .brand-line { font-size: 12px; }
  .ad-skyscraper .headline { position: absolute; top: 134px; left: 0; width: 100%; }
  .ad-skyscraper .headline .lead { font-size: 29px; }
  .ad-skyscraper .headline .sub { font-size: 25px; }
  .ad-skyscraper .tagline { position: absolute; top: 222px; left: 6px; right: 6px; font-size: 14px; line-height: 19px; }
  .ad-skyscraper .rule-top { left: 0; top: 330px; width: 100%; height: 5px; }
  .ad-skyscraper .photo { left: 0; top: 335px; width: 100%; height: 288px; }
  .ad-skyscraper .rule-bottom { left: 0; top: 623px; width: 100%; height: 5px; }
  .ad-skyscraper .cta { left: 9px; top: 658px; width: 171px; height: 39px; font-size: 16px; }

  /* Leaderboard */
  .ad-leaderboard .copy { position: absolute; left: 0; top: 0; width: 297px; height: 100%; padding-top: 4px; }
  .ad-leaderboard .headline .lead { font-size: 43px; }
  .ad-leaderboard .headline .sub { font-size: 20px; }
  .ad-leaderboard .tagline { font-size: 13px; line-height: 17px; margin-top: 3px; }
  .ad-leaderboard .rule-left { left: 297px; top: 0; width: 4px; height: 100%; }
  .ad-leaderboard .photo { left: 301px; top: 0; width: 366px; height: 100%; }
  .ad-leaderboard .rule-right { left: 667px; top: 0; width: 4px; height: 100%; }
  .ad-leaderboard .brand { left: 718px; top: 10px; }
  .ad-leaderboard .brand-name { font-size: 19px; }
  .ad-leaderboard .brand-mark { width: 7px; height: 7px; }
  .ad-leaderboard .brand-line { font-size: 10px; }
  .ad-leaderboard .cta { left: 689px; top: 61px; width: 170px; height: 40px; font-size: 16px; }

  /* Square */
  .ad-square .headline { position: absolute; top: 8px; left: 0; width: 100%; }
  .ad-square .headline .lead { font-size: 51px; }
  .ad-square .headline .sub { font-size: 24px; }
  .ad-square .tagline { position: absolute; top: 80px; left: 0; width: 100%; font-size: 15px; line-height: 20px; }
  .ad-square .rule-top { left: 0; top: 128px; width: 100%; height: 5px; }
  .ad-square .photo { left: 0; top: 133px; width: 100%; height: 138px; }
  .ad-square .rule-bottom { left: 0; top: 271px; width: 100%; height: 5px; }
  .ad-square .brand { left: 26px; top: 288px; }
  .ad-square .brand-name { font-size: 19px; }
  .ad-square .brand-mark { width: 7px; height: 7px; }
  .ad-square .brand-line { font-size: 10px; }
  .ad-square .cta { left: 216px; top: 287px; width: 170px; height: 40px; font-size: 16px; }
</style>
</head>
<body>

  <section class="ad ad-skyscraper" aria-label="Skyscraper banner">
    <div class="brand">
      <span class="brand-name">oak-ferry<span class="brand-mark"></span></span>
      <span class="brand-line">Information Security</span>
    </div>
    <h1 class="headline"><span class="lead">One-Time</span><span class="sub">Shredding</span><span class="sub">Services</span></h1>
    <p class="tagline">Your Paper Can be Destroyed as Soon as the Next Business Day</p>
    <div class="rule rule-top"></div>
    <div class="photo" role="img" aria-label="Hand sliding a stack of paper into a secure shredding console in an office"></div>
    <div class="rule rule-bottom"></div>
    <a class="cta" href="#">Get a Quote
      <svg width="9" height="11" viewBox="0 0 9 11" aria-hidden="true"><path d="M0 0 L9 5.5 L0 11 Z" fill="#fff"/></svg>
    </a>
  </section>

  <section class="ad ad-leaderboard" aria-label="Leaderboard banner">
    <div class="copy">
      <h2 class="headline"><span class="lead">One-Time</span><span class="sub">Shredding Services</span></h2>
      <p class="tagline">Your Paper Can be Destroyed as<br>Soon as the Next Business Day</p>
    </div>
    <div class="rule rule-left"></div>
    <div class="photo" role="img" aria-label="Hand sliding a stack of paper into a secure shredding console in an office"></div>
    <div class="rule rule-right"></div>
    <div class="brand">
      <span class="brand-name">oak-ferry<span class="brand-mark"></span></span>
      <span class="brand-line">Information Security</span>
    </div>
    <a class="cta" href="#">Get a Quote
      <svg width="9" height="11" viewBox="0 0 9 11" aria-hidden="true"><path d="M0 0 L9 5.5 L0 11 Z" fill="#fff"/></svg>
    </a>
  </section>

  <section class="ad ad-square" aria-label="Square banner">
    <h2 class="headline"><span class="lead">One-Time</span><span class="sub">Shredding Services</span></h2>
    <p class="tagline">Your Paper Can be Destroyed as<br>Soon as the Next Business Day</p>
    <div class="rule rule-top"></div>
    <div class="photo" role="img" aria-label="Hand sliding a stack of paper into a secure shredding console in an office"></div>
    <div class="rule rule-bottom"></div>
    <div class="brand">
      <span class="brand-name">oak-ferry<span class="brand-mark"></span></span>
      <span class="brand-line">Information Security</span>
    </div>
    <a class="cta" href="#">Get a Quote
      <svg width="9" height="11" viewBox="0 0 9 11" aria-hidden="true"><path d="M0 0 L9 5.5 L0 11 Z" fill="#fff"/></svg>
    </a>
  </section>

</body>
</html>
```